KORVa: AI driven decarbonization application

We are seeking an engaging, user-friendly, and visually appealing user interface for our B2B SaaS platform, Brelmont KORVa. This solution helps large organizations achieve net-zero emissions using AI-driven forecasting, AI models, a emission mitigation library, and a scenario simulator..

A big challenge is to allow the user to work efficiently with multidimensional data.

Requirements:

* Design a modern, professional, and visually striking user interface, catering to a diverse audience within large corporations, including executives, strategists, and environmental specialists.

* Construct an intuitive navigation system, allowing users to seamlessly access functionalities for informed decision-making and tracking progress towards net-zero emissions.

* The application is expected to be used on desktops first

* Incorporate our brand's colors, and visual elements into the design to maintain consistency throughout the application.

* Provide design assets and documentation, such as style guides, design specifications, and necessary assets (e.g., icons, illustrations) for our development team to implement the design. We use Figma and would appreciate delivery as figma files.

Please note that we also need more pages over time. The most important is to get the work bench page right. We will also need:
* a landing page where the users can select previous scenarios and see some high level data.
* A page with information on historical data per asset
* An analytics page
* User and system administration pages.
These pages are out of scope for this project, but they should be available in the navigation solution.

Please submit your initial design concepts, accompanied by a brief explanation of your approach and the rationale behind your design choices. We will offer feedback and collaborate with the chosen designer to refine the design, ensuring it meets our requirements and vision.

We are really hoping to see some elegant user interfaces. The functionality describe in the attachment is important, but the layout is not. Feel free to invent.

Attached files:

Target Market(s)

Energy intensive industries

Requirements
Must have
• Easy to navigate through the different data dimensions: Time, assets, mitigation measures, and advanced details under mitigation measures. The design in the attached files are just our working drafts. Creative alternatives are very welcome.
Nice to have
• Elegant layouts that differ from our working drafts.

```html
<!DOCTYPE html>
<html lang="en">
<head>
<meta charset="utf-8">
<title>Brelmont KORVa – Scenario Simulation</title>
<link href="https://fonts.googleapis.com/css2?family=Poppins:wght@400;500;600&display=swap" rel="stylesheet">
<style>
:root{
  --navy:#124a7a;
  --side-top:#154a7a;
  --side-bottom:#2f7fc0;
  --page:#eef5fc;
  --card:#ffffff;
  --ink:#1d2b3a;
  --muted:#8a94a0;
  --line-dark:#1a5fa0;
  --line-teal:#5c9a9a;
  --blue-dark:#2a6fae;
  --blue-mid:#4da6ef;
  --blue-light:#cfe6fb;
  --teal-btn:#5f9f9d;
  --card-navy:#0f3a63;
  --card-blue:#2c75b5;
  --card-sky:#5aaef5;
}
*{box-sizing:border-box;margin:0;padding:0}
html,body{width:1200px;height:853px;overflow:hidden;background:var(--page);font-family:"Poppins",sans-serif;color:var(--ink)}
.canvas{position:relative;width:1200px;height:853px;overflow:hidden}
.stage{position:absolute;left:0;top:0;width:1440px;height:1024px;transform:scale(.83334);transform-origin:0 0;background:var(--page)}
.abs{position:absolute}
.sidebar{left:0;top:0;width:315px;height:1024px;background:linear-gradient(180deg,var(--side-top),var(--side-bottom));color:#fff}
.brand{left:52px;top:58px;font-size:29px;font-weight:400;letter-spacing:3px}
.nav-group{left:38px;width:260px;display:flex;align-items:center;gap:12px;font-size:15px;font-weight:600;letter-spacing:.3px}
.nav-group svg{flex:none}
.nav-group .chev{position:absolute;right:0}
.carrier-item{left:83px;width:210px;font-size:15.5px;display:flex;justify-content:space-between;align-items:center}
.box{width:10px;height:10px;border:1.5px solid #fff;border-radius:1px}
.box.on{background:#fff}
.report{left:80px;top:877px;font-size:14px;font-weight:600;display:flex;gap:10px;align-items:center}
.download{left:65px;top:917px;width:144px;height:40px;border-radius:4px;background:var(--teal-btn);color:#fff;font-size:14px;display:flex;align-items:center;justify-content:center}
.topbar{left:315px;top:0;width:1125px;height:80px;background:var(--navy);color:#dfe9f3}
.topnav{position:absolute;top:30px;font-size:16px}
.topnav.active{color:#fff}
.topnav.active::after{content:"";position:absolute;left:-2px;right:-2px;top:46px;height:3px;background:#fff}
.divider{left:527px;top:22px;width:1px;height:36px;background:#fff;opacity:.6}
.user{left:778px;top:28px;font-size:18px;color:#fff}
.avatar{left:927px;top:15px;width:50px;height:50px;border-radius:12px;background:linear-gradient(135deg,#c9a27a,#6d4b34)}
.card{background:var(--card);border-radius:10px}
.crumb{font-size:11px;color:var(--blue-dark)}
.crumb span{color:#b2b9c1;margin-left:30px}
.title{left:463px;top:186px;font-size:25px;font-weight:600}
.chart-title{left:401px;top:263px;font-size:16.5px;font-weight:500}
.axis{font-size:13px;color:#9aa3ad}
.select{left:1138px;top:241px;width:115px;height:29px;border:1px solid #e2e7ec;border-radius:3px;font-size:14px;padding:4px 9px}
.more{left:1282px;top:241px;width:28px;height:28px;border:1px solid #e2e7ec;border-radius:4px;font-size:12px;text-align:center;line-height:22px;color:#445}
.tooltip{left:752px;top:326px;width:155px;height:73px;background:#fff;border-radius:6px;box-shadow:0 6px 20px rgba(20,50,80,.12);padding:14px 18px}
.panel-title{font-size:14px;font-weight:600}
.legend{font-size:12.5px;display:flex;align-items:center;gap:9px}
.legend b{font-weight:600}
.legend span{color:#6c7681}
.bars{left:754px;top:711px;display:flex;gap:17px}
.bar{width:17px;height:119px;border-radius:9px;overflow:hidden;display:flex;flex-direction:column;background:var(--blue-light)}
.bar i{display:block}
.seg-mid{background:var(--blue-mid)}
.seg-light{background:var(--blue-light)}
.seg-dark{background:var(--blue-dark);flex:1}
.barlabels{left:750px;top:846px;display:flex;font-size:11px;color:#55606b}
.barlabels span{width:34.4px;text-align:center}
.rate-row{left:1175px;width:171px;display:flex;justify-content:space-between;font-size:14px}
.rate-row b{font-weight:600}
.rate-sub{left:1175px;width:169px;display:flex;justify-content:space-between;font-size:10px;color:#7d8793}
.stat{top:937px;width:321px;height:87px;border-radius:14px 14px 0 0;color:#fff;overflow:hidden}
.stat .ico{position:absolute;left:23px;top:24px;width:58px;height:58px;border-radius:10px;background:rgba(255,255,255,.14);display:flex;align-items:center;justify-content:center}
.stat .lbl{position:absolute;left:98px;top:29px;font-size:13.5px;opacity:.9}
.stat .val{position:absolute;left:98px;top:55px;font-size:20px;font-weight:600}
.stat .arr{position:absolute;right:22px;top:64px}
</style>
</head>
<body>
<div class="canvas">
<div class="stage">
  <aside class="abs sidebar">
    <div class="abs brand">BRELMONT</div>

    <div class="abs nav-group" style="top:208px">
      <svg width="24" height="24" viewBox="0 0 24 24" fill="none" stroke="#fff" stroke-width="1.3"><circle cx="12" cy="12" r="10"/><path d="M13 5l-5 8h4l-1 6 5-8h-4z"/></svg>
      SWITCH ENERGY CARRIER
      <svg class="chev" width="12" height="8" viewBox="0 0 12 8" fill="none" stroke="#fff" stroke-width="1.5"><path d="M1 7l5-5 5 5"/></svg>
    </div>
    <div class="abs carrier-item" style="top:250px">Biodiesel <i class="box on"></i></div>
    <div class="abs carrier-item" style="top:284px">Ethanol <i class="box"></i></div>
    <div class="abs carrier-item" style="top:318px">Hydrogen <i class="box"></i></div>
    <div class="abs carrier-item" style="top:352px">Methanol <i class="box"></i></div>
    <div class="abs carrier-item" style="top:386px">Power offshore wind <i class="box"></i></div>
    <div class="abs carrier-item" style="top:420px">Power form shore <i class="box"></i></div>

    <div class="abs nav-group" style="top:500px">
      <svg width="24" height="24" viewBox="0 0 24 24" fill="none" stroke="#fff" stroke-width="1.3"><path d="M3 22V14h3v8M9 22V10h3v12M15 22V12h3v10M20 22V6h2v16M3 9l6-5 5 3 7-5"/></svg>
      ENERGY EFFICIENCY
      <svg class="chev" width="12" height="8" viewBox="0 0 12 8" fill="none" stroke="#fff" stroke-width="1.5"><path d="M1 1l5 5 5-5"/></svg>
    </div>
    <div class="abs nav-group" style="top:556px">
      <svg width="24" height="28" viewBox="0 0 24 28" fill="none" stroke="#fff" stroke-width="1.3"><rect x="2" y="2" width="20" height="24" rx="2"/><path d="M6 8h12M6 13h12M6 18h8"/></svg>
      LOGISTICS
      <svg class="chev" width="12" height="8" viewBox="0 0 12 8" fill="none" stroke="#fff" stroke-width="1.5"><path d="M1 1l5 5 5-5"/></svg>
    </div>
    <div class="abs nav-group" style="top:606px">
      <svg width="24" height="24" viewBox="0 0 24 24" fill="none" stroke="#fff" stroke-width="1.3"><path d="M3 21h18M5 21V8h3v13M10 21v-8h10v8M12 6c0-2 3-2 3-4"/></svg>
      END OF PIPE MEASURES
      <svg class="chev" width="12" height="8" viewBox="0 0 12 8" fill="none" stroke="#fff" stroke-width="1.5"><path d="M1 1l5 5 5-5"/></svg>
    </div>
    <div class="abs nav-group" style="top:660px">
      <svg width="24" height="26" viewBox="0 0 24 26" fill="none" stroke="#fff" stroke-width="1.3"><rect x="2" y="8" width="20" height="16" rx="1"/><path d="M7 8V4h10v4M8 16l3 3 5-6"/></svg>
      CARBON OFFSETS
      <svg class="chev" width="12" height="8" viewBox="0 0 12 8" fill="none" stroke="#fff" stroke-width="1.5"><path d="M1 1l5 5 5-5"/></svg>
    </div>
    <div class="abs nav-group" style="top:717px">
      <svg width="26" height="28" viewBox="0 0 26 28" fill="none" stroke="#fff" stroke-width="1.3"><rect x="3" y="10" width="20" height="16"/><path d="M8 10V3h10v7M7 15h3M12 15h3M17 15h3M7 20h3M17 20h3M11 26v-5h4v5"/></svg>
      COMPANY STRUCTURE
      <svg class="chev" width="12" height="8" viewBox="0 0 12 8" fill="none" stroke="#fff" stroke-width="1.5"><path d="M1 1l5 5 5-5"/></svg>
    </div>

    <div class="abs report">Monthly Report
      <svg width="14" height="9" viewBox="0 0 14 9" fill="none" stroke="#fff" stroke-width="1.8"><path d="M1 1l6 6 6-6"/></svg>
    </div>
    <div class="abs download">Download</div>
  </aside>

  <header class="abs topbar">
    <span class="topnav" style="left:66px">Home</span>
    <span class="topnav" style="left:154px">Assets</span>
    <span class="topnav active" style="left:246px">Scenario&nbsp; Simulation</span>
    <span class="topnav" style="left:450px">Map</span>
    <div class="abs divider"></div>
    <svg class="abs" style="left:570px;top:30px" width="21" height="21" viewBox="0 0 21 21" fill="none" stroke="#fff" stroke-width="1.8"><circle cx="9" cy="9" r="7"/><path d="M14 14l5 5"/></svg>
    <div class="abs user">Dana Whitfield</div>
    <div class="abs avatar" role="img" aria-label="User profile photo"></div>
    <svg class="abs" style="left:993px;top:37px" width="8" height="5" viewBox="0 0 8 5" fill="none" stroke="#cfe" stroke-width="1.2"><path d="M1 1l3 3 3-3"/></svg>
  </header>

  <section class="abs card" style="left:362px;top:110px;width:1010px;height:526px"></section>
  <div class="abs crumb" style="left:401px;top:156px">DASHBOARD <span>Switch energy Carrier</span></div>
  <div class="abs" style="left:401px;top:181px;width:42px;height:42px;border-radius:10px;background:#1f2a36"></div>
  <div class="abs title">Brelmont</div>
  <div class="abs" style="left:604px;top:183px;font-size:26px;font-weight:500">+</div>
  <div class="abs" style="left:645px;top:181px;width:42px;height:42px;border-radius:50%;background:#f1f5fb"></div>
  <div class="abs chart-title">Relative Emissions, Kg CO2e /&nbsp; produced unit</div>
  <svg class="abs" style="left:792px;top:266px" width="15" height="15" viewBox="0 0 15 15" fill="none" stroke="#c3c9cf"><circle cx="7.5" cy="7.5" r="6.5"/><path d="M7.5 6.5v4M7.5 4v1"/></svg>
  <div class="abs" style="left:927px;top:255px;width:58px;height:3px;background:#cfe0e0;border-radius:2px"></div>
  <div class="abs" style="left:1013px;top:248px;font-size:11px;color:#c5ccd3">Provisions Month</div>
  <div class="abs select">May 2023
    <svg style="position:absolute;right:10px;top:8px" width="12" height="12" viewBox="0 0 12 12" fill="none" stroke="#1a5fa0"><rect x="1" y="2" width="10" height="9"/><path d="M1 5h10M4 1v2M8 1v2"/></svg>
  </div>
  <div class="abs more">•••</div>

  <div class="abs axis" style="left:400px;top:320px">260M</div>
  <div class="abs axis" style="left:400px;top:388px">220M</div>
  <div class="abs axis" style="left:400px;top:457px">180M</div>
  <div class="abs axis" style="left:400px;top:525px">140M</div>
  <div class="abs axis" style="left:462px;top:556px">1</div>
  <div class="abs axis" style="left:603px;top:556px">5</div>
  <div class="abs axis" style="left:742px;top:556px">10</div>
  <div class="abs axis" style="left:885px;top:556px">15</div>
  <div class="abs axis" style="left:1028px;top:556px">20</div>
  <div class="abs axis" style="left:1171px;top:556px">25</div>
  <div class="abs axis" style="left:1297px;top:556px">30</div>

  <svg class="abs" style="left:0;top:0;pointer-events:none" width="1440" height="1024" viewBox="0 0 1440 1024" fill="none">
    <g stroke="#eef1f4" stroke-width="1">
      <path d="M462 345H1305M462 414H1305M462 482H1305M462 550H1305"/>
    </g>
    <path d="M835 430V550" stroke="#55606b" stroke-dasharray="3 3"/>
    <path stroke="var(--line-teal)" stroke-width="1.6" d="M462 458C500 452 515 470 540 482C575 498 620 495 650 475C680 455 700 450 720 425C745 395 770 390 800 400C830 410 850 430 890 436C930 442 950 480 990 498C1030 515 1090 510 1110 500C1140 480 1160 450 1190 460C1220 470 1240 490 1260 498C1285 508 1300 506 1315 507"/>
    <path stroke="var(--line-dark)" stroke-width="1.8" d="M462 518C500 510 520 485 545 478C580 470 600 498 650 496C690 494 710 510 725 498C745 482 760 455 790 450C820 446 825 440 840 420C860 392 880 382 910 383C950 384 960 385 975 398C995 416 1010 410 1030 392C1060 365 1090 350 1120 358C1150 367 1170 405 1200 430C1225 452 1240 475 1260 462C1280 448 1295 448 1315 448"/>
    <circle cx="829" cy="427" r="6" fill="#1f74c0" stroke="#fff" stroke-width="2"/>
  </svg>

  <div class="abs tooltip">
    <div style="font-size:7px;color:#8a94a0">This Month</div>
    <div style="font-size:20px;font-weight:600;line-height:1.25">220,342,123</div>
    <div style="font-size:12px;color:#8a94a0">May</div>
  </div>

  <section class="abs card" style="left:359px;top:661px;width:320px;height:242px"></section>
  <div class="abs panel-title" style="left:380px;top:682px">Our Ratio</div>
  <svg class="abs" style="left:0;top:0;pointer-events:none" width="1440" height="1024" viewBox="0 0 1440 1024">
    <circle cx="455" cy="792" r="65" fill="none" stroke="#1e5f9c" stroke-width="28"/>
    <circle cx="455" cy="792" r="65" fill="none" stroke="#aad5fb" stroke-width="28" stroke-dasharray="163.4 245"/>
    <rect x="480" y="723" width="30" height="15" rx="7" fill="#fff"/>
    <rect x="396" y="839" width="30" height="15" rx="7" fill="#fff"/>
  </svg>
  <div class="abs" style="left:483px;top:725px;font-size:9px">60%</div>
  <div class="abs" style="left:400px;top:841px;font-size:9px">40%</div>
  <div class="abs legend" style="left:546px;top:771px"><i style="width:17px;height:9px;background:#1e5f9c"></i><b>60%</b><span>Visitors</span></div>
  <div class="abs legend" style="left:546px;top:806px"><i style="width:17px;height:9px;background:#cfe6fb"></i><b>&nbsp;40%</b><span>Visitors</span></div>

  <section class="abs card" style="left:700px;top:661px;width:436px;height:242px"></section>
  <div class="abs panel-title" style="left:719px;top:682px">Our Project &amp; &nbsp;Level</div>
  <div class="abs" style="left:720px;top:703px;font-size:10px;color:#55606b;line-height:27.3px;text-align:right;width:22px">100<br>75<br>50<br>25<br>0</div>
  <div class="abs bars">
    <div class="bar"><i class="seg-mid" style="height:101px"></i><i class="seg-dark"></i></div>
    <div class="bar" style="background:#fff"><i class="seg-mid" style="height:81px"></i><i class="seg-light" style="height:28px"></i></div>
    <div class="bar"><i class="seg-mid" style="height:65px"></i><i class="seg-light" style="height:40px"></i><i class="seg-dark"></i></div>
    <div class="bar"><i class="seg-mid" style="height:31px"></i><i class="seg-light" style="height:20px"></i><i class="seg-dark"></i></div>
    <div class="bar"><i class="seg-mid" style="height:30px"></i><i class="seg-light" style="height:51px"></i><i class="seg-dark"></i></div>
    <div class="bar"><i class="seg-mid" style="height:43px"></i><i class="seg-light" style="height:30px"></i><i class="seg-dark"></i></div>
    <div class="bar"><i class="seg-mid" style="height:30px"></i><i class="seg-light" style="height:29px"></i><i class="seg-dark"></i></div>
    <div class="bar"><i class="seg-light" style="height:85px"></i><i class="seg-dark"></i></div>
    <div class="bar"><i class="seg-light" style="height:101px"></i><i class="seg-dark"></i></div>
    <div class="bar"><i class="seg-mid" style="height:38px"></i><i class="seg-light" style="height:59px"></i><i class="seg-dark"></i></div>
    <div class="bar"><i class="seg-mid" style="height:38px"></i><i class="seg-light" style="height:47px"></i><i class="seg-dark"></i></div>
  </div>
  <div class="abs barlabels">
    <span>JHK</span><span>FHG</span><span>LSL</span><span>DLD</span><span>USI</span><span>SKA</span><span>AAL</span><span>FFR</span><span>JHY</span><span>UYT</span><span>JKJ</span>
  </div>
  <div class="abs" style="left:771px;top:872px;font-size:12px;font-weight:600;display:flex;gap:22px">
    <span><span style="color:#2a6fae">●</span> Completed</span>
    <span><span style="color:var(--line-teal)">●</span> In progress</span>
    <span><span style="color:#3a98e6">●</span> Fired</span>
  </div>

  <section class="abs card" style="left:1157px;top:661px;width:212px;height:242px"></section>
  <div class="abs panel-title" style="left:1170px;top:682px">Our Rates</div>
  <div class="abs rate-row" style="top:714px">MQL <b>3 456</b></div>
  <div class="abs rate-sub" style="top:736px">Conversion rate <span>71%</span></div>
  <div class="abs rate-row" style="top:759px;left:1177px;width:169px">SQL <b>2456</b></div>
  <div class="abs rate-sub" style="top:780px;left:1177px;width:167px">Conversion rate <span>38%</span></div>
  <div class="abs rate-row" style="top:808px;left:1177px;width:169px">Meeting <b>956</b></div>
  <div class="abs rate-sub" style="top:828px;left:1177px;width:167px">Conversion rate <span>59%</span></div>
  <div class="abs rate-row" style="top:855px;left:1177px;width:169px">Sells <b>567</b></div>

  <div class="abs stat" style="left:350px;background:var(--card-navy)">
    <div class="ico"><svg width="24" height="26" viewBox="0 0 24 26" fill="none" stroke="#fff" stroke-width="1.4"><rect x="3" y="2" width="18" height="22" rx="2"/><path d="M7 8h10M7 13h10M7 18h6"/></svg></div>
    <div class="lbl">SALES</div><div class="val">455k</div>
    <svg class="arr" width="18" height="10" viewBox="0 0 18 10" fill="none" stroke="#fff" stroke-width="1.3"><path d="M1 5h16M12 1l5 4-5 4"/></svg>
  </div>
  <div class="abs stat" style="left:695px;background:var(--card-blue)">
    <div class="ico"><svg width="28" height="28" viewBox="0 0 28 28" fill="none" stroke="#fff" stroke-width="1.4"><circle cx="14" cy="14" r="11"/><path d="M14 3v22M14 14h11"/></svg></div>
    <div class="lbl">Total Profit</div><div class="val">520 k</div>
    <svg class="arr" width="18" height="10" viewBox="0 0 18 10" fill="none" stroke="#fff" stroke-width="1.3"><path d="M1 5h16M12 1l5 4-5 4"/></svg>
  </div>
  <div class="abs stat" style="left:1039px;width:322px;background:var(--card-sky)">
    <div class="ico"><svg width="26" height="24" viewBox="0 0 26 24" fill="none" stroke="#fff" stroke-width="1.4"><rect x="3" y="4" width="20" height="16" rx="2"/><rect x="9" y="8" width="10" height="8"/><circle cx="14" cy="12" r="2"/></svg></div>
    <div class="lbl">Business Cost</div><div class="val">560 k</div>
    <svg class="arr" width="18" height="10" viewBox="0 0 18 10" fill="none" stroke="#fff" stroke-width="1.3"><path d="M1 5h16M12 1l5 4-5 4"/></svg>
  </div>

  <div class="abs" style="left:1432px;top:125px;width:6px;height:255px;border-radius:3px;background:#d8e6f3"></div>
</div>
</div>
</body>
</html>
```